Structural Engineering Business Card

Veltrow Drafts does residential house plans for clients in Central Florida. Would like simple but elegant business card that is appropriate for a house plan engineering company. Prefer black business card with black/white them but open to other shades of blue. I uploaded a sample card that I came across that looked good but please come up with your own creative designs.

Contact Information for Business Card

Name, Title, Phone, Email, Address, website

```html
<!DOCTYPE html>
<html lang="en">
<head>
<meta charset="utf-8">
<title>Veltrow Drafts — Business Card</title>
<link href="https://fonts.googleapis.com/css2?family=Montserrat:wght@400;600;800&display=swap" rel="stylesheet">
<style>
  :root {
    --page: #2a2b2e;
    --navy-deep: #0b1226;
    --navy: #0f1d3d;
    --teal: #1fa59a;
    --teal-soft: #1d6f6c;
    --white: #ffffff;
    --muted: #b8c2d3;
  }
  * { box-sizing: border-box; margin: 0; padding: 0; }
  html, body { width: 1200px; height: 817px; overflow: hidden; }
  body {
    background: var(--page);
    font-family: "Montserrat", sans-serif;
    display: flex;
    align-items: center;
    justify-content: center;
    gap: 40px;
  }
  .card {
    position: relative;
    width: 525px;
    height: 300px;
    border-radius: 26px;
    overflow: hidden;
    box-shadow: 0 18px 40px rgba(0,0,0,.45);
  }
  .card--front {
    background: linear-gradient(135deg, var(--navy) 0%, var(--navy-deep) 70%);
  }
  .card--back {
    background: linear-gradient(160deg, var(--navy-deep) 0%, var(--navy) 100%);
  }
  .blueprint-front {
    position: absolute;
    right: 0; top: 0;
    width: 260px; height: 240px;
    background: radial-gradient(ellipse at 75% 25%, rgba(31,165,154,.35) 0%, rgba(29,111,108,.15) 45%, rgba(15,29,61,0) 75%);
  }
  .blueprint-back {
    position: absolute;
    left: 150px; bottom: 0;
    width: 340px; height: 130px;
    background: radial-gradient(ellipse at 50% 90%, rgba(31,165,154,.16) 0%, rgba(15,29,61,0) 70%);
  }
  .wordmark {
    position: absolute;
    color: var(--white);
    font-weight: 800;
    font-size: 30px;
    letter-spacing: .5px;
    text-transform: uppercase;
    line-height: 1;
    white-space: nowrap;
  }
  .card--front .wordmark { left: 44px; top: 150px; }
  .card--back .wordmark { left: 40px; top: 228px; }
  .contact {
    position: absolute;
    left: 262px; top: 30px;
    color: var(--white);
  }
  .contact__name {
    font-weight: 800;
    font-size: 17px;
    letter-spacing: .4px;
    text-transform: uppercase;
  }
  .contact__title {
    font-weight: 400;
    font-size: 13px;
    color: var(--muted);
    margin-top: 2px;
  }
  .contact__rule {
    width: 62px; height: 2px;
    background: var(--teal);
    margin: 9px 0 14px;
  }
  .contact__list { list-style: none; }
  .contact__item {
    display: flex;
    align-items: flex-start;
    gap: 10px;
    font-size: 11.5px;
    line-height: 1.35;
    margin-bottom: 9px;
  }
  .contact__item:last-child { margin-bottom: 0; }
  .icon {
    flex: none;
    width: 18px; height: 18px;
    background: var(--teal);
    border-radius: 3px;
    display: flex; align-items: center; justify-content: center;
  }
  .icon svg { width: 11px; height: 11px; }
</style>
</head>
<body>

<section class="card card--front">
  <div class="blueprint-front" role="img" aria-label="Faint teal architectural blueprint of a house roof and plan lines"></div>
  <span class="wordmark">Veltrow Drafts</span>
</section>

<section class="card card--back">
  <div class="blueprint-back" role="img" aria-label="Faint blueprint elevation drawing of a house"></div>

  <div class="contact">
    <p class="contact__name">Dorian M. Hale</p>
    <p class="contact__title">Managing Director</p>
    <div class="contact__rule"></div>
    <ul class="contact__list">
      <li class="contact__item">
        <span class="icon"><svg viewBox="0 0 12 12"><path d="M6 1a3.5 3.5 0 0 0-3.5 3.5C2.5 7.5 6 11 6 11s3.5-3.5 3.5-6.5A3.5 3.5 0 0 0 6 1zm0 4.8a1.3 1.3 0 1 1 0-2.6 1.3 1.3 0 0 1 0 2.6z" fill="#fff"/></svg></span>
        <span>2170 Larkspur Avenue<br>Florida, U.S. 32801</span>
      </li>
      <li class="contact__item">
        <span class="icon"><svg viewBox="0 0 12 12"><path d="M3 1.5l1.6 2.4-1 1c.6 1.3 1.6 2.3 2.9 2.9l1-1L10 8.4 9 10.5C5 10.2 1.8 7 1.5 3z" fill="#fff"/></svg></span>
        <span>+00 321 654 90</span>
      </li>
      <li class="contact__item">
        <span class="icon"><svg viewBox="0 0 12 12"><rect x="1.5" y="3" width="9" height="6" fill="none" stroke="#fff" stroke-width="1.1"/><path d="M1.5 3L6 6.5 10.5 3" fill="none" stroke="#fff" stroke-width="1.1"/></svg></span>
        <span>studio@veltrowdrafts.com</span>
      </li>
      <li class="contact__item">
        <span class="icon"><svg viewBox="0 0 12 12"><path d="M2.5 2l7 3-3 1-1 3z" fill="#fff"/></svg></span>
        <span>www.veltrowdrafts.com</span>
      </li>
    </ul>
  </div>

  <span class="wordmark">Veltrow Drafts</span>
</section>

</body>
</html>
```